Consulting and investment firm, logo design is needed as well.

I am looking to open a consulting firm. Where myself is currently an investor, entrepreneur and consultant for many businesses.

The company name is Torvique Company Limited
The logo should communicate prestige like luxury or gold or money, trustworthy and modern.

Overall name card Color can be: white, black, blue, gold, silver (you can choose one, few or all of it, up to you)

It would be great if you can provide raw file like .psd for me so that I can make some little amendment in future and inserting company name or remove it. Because I would also like to use it as only under my name too (some card I will remove the company name).

• I want it to look modern.

```html
<!DOCTYPE html>
<html lang="en">
<head>
<meta charset="utf-8">
<title>Torvique Company Limited – Business Card</title>
<link href="https://fonts.googleapis.com/css2?family=Montserrat:wght@700;800&family=Poppins:wght@400;500&display=swap" rel="stylesheet">
<style>
  :root{
    --bg:#2a2a2a;
    --card:#050505;
    --gold:#f7b225;
    --silver:#b3b3b3;
    --white:#ffffff;
    --text:#e6e6e6;
    --phone:#9ccc3c;
  }
  *{margin:0;padding:0;box-sizing:border-box}
  html,body{width:1200px;height:900px;overflow:hidden;background:var(--bg)}
  .stage{position:relative;width:1200px;height:900px}
  .card{
    position:absolute;width:700px;height:400px;background:var(--card);
    border-radius:22px;overflow:hidden;box-shadow:0 12px 30px rgba(0,0,0,.5);
  }
  .card--back{left:60px;top:40px}
  .card--front{left:440px;top:460px}

  .wordmark{font-family:"Montserrat",sans-serif;font-weight:800;color:var(--white);text-transform:uppercase;line-height:1}
  .card--back .brand{position:absolute;left:0;right:0;top:0;bottom:0;display:flex;align-items:center;justify-content:center;gap:22px}
  .brand__dot{width:74px;height:74px;border-radius:50%;background:var(--gold);flex:none}
  .card--back .wordmark__name{font-size:44px;letter-spacing:5px}
  .card--back .wordmark__sub{font-size:17px;letter-spacing:3px;margin-top:6px}

  .front__info{position:absolute;left:46px;top:52px;width:400px}
  .card--front .wordmark__name{font-size:52px;letter-spacing:5px}
  .card--front .wordmark__sub{font-size:20px;letter-spacing:3px;margin-top:6px}
  .person{margin-top:36px}
  .person__name{font-family:"Montserrat",sans-serif;font-weight:700;font-size:30px;letter-spacing:2px;color:var(--silver);text-transform:uppercase;line-height:1}
  .person__role{font-family:"Montserrat",sans-serif;font-weight:700;font-size:15px;letter-spacing:1.5px;color:var(--gold);text-transform:uppercase;margin-top:6px}
  .contact{list-style:none;margin-top:22px;font-family:"Poppins",sans-serif;font-size:14px;color:var(--text)}
  .contact li{display:flex;align-items:flex-start;gap:10px;line-height:1.45}
  .contact svg{width:14px;height:14px;flex:none;margin-top:3px}
  .contact .address{margin-top:8px}

  .front__decor{position:absolute;right:-120px;top:20px;width:420px;height:420px;border-radius:50%;background:var(--gold)}
</style>
</head>
<body>
<div class="stage">

  <section class="card card--back">
    <div class="brand">
      <span class="brand__dot"></span>
      <div class="wordmark">
        <div class="wordmark__name">Torvique</div>
        <div class="wordmark__sub">Company Limited</div>
      </div>
    </div>
  </section>

  <section class="card card--front">
    <div class="front__decor"></div>
    <div class="front__info">
      <div class="wordmark">
        <div class="wordmark__name">Torvique</div>
        <div class="wordmark__sub">Company Limited</div>
      </div>
      <div class="person">
        <div class="person__name">Marcus Ellery</div>
        <div class="person__role">Managing Director</div>
      </div>
      <ul class="contact">
        <li>
          <svg viewBox="0 0 24 24"><path fill="var(--phone)" d="M6.6 10.8a15 15 0 0 0 6.6 6.6l2.2-2.2c.3-.3.7-.4 1-.2 1.1.4 2.3.6 3.6.6.6 0 1 .4 1 1V20c0 .6-.4 1-1 1A17 17 0 0 1 3 4c0-.6.4-1 1-1h3.5c.6 0 1 .4 1 1 0 1.3.2 2.5.6 3.6.1.3 0 .7-.2 1z"/></svg>
          <span>555 218 0937</span>
        </li>
        <li>
          <svg viewBox="0 0 24 24"><rect x="2" y="5" width="20" height="14" fill="none" stroke="var(--gold)" stroke-width="2"/><path d="M2 5l10 8 10-8" fill="none" stroke="var(--gold)" stroke-width="2"/></svg>
          <span>info@torviquecompanylimited.com</span>
        </li>
        <li>
          <svg viewBox="0 0 24 24"><g fill="none" stroke="var(--gold)" stroke-width="2"><circle cx="12" cy="12" r="10"/><ellipse cx="12" cy="12" rx="4" ry="10"/><path d="M2 12h20"/></g></svg>
          <span>www.torviquecompanylimited.com</span>
        </li>
        <li class="address">
          <svg viewBox="0 0 24 24"><path fill="var(--gold)" d="M12 2a7 7 0 0 0-7 7c0 5 7 13 7 13s7-8 7-13a7 7 0 0 0-7-7zm0 9.5A2.5 2.5 0 1 1 12 6.5a2.5 2.5 0 0 1 0 5z"/></svg>
          <span>118 Larkspur Avenue NW<br>Suite 400, Fairhaven<br>MI 49210</span>
        </li>
      </ul>
    </div>
  </section>

</div>
</body>
</html>
```